Copperline Wiring Vehicle Van Wrap Design

We need a new vehicle wrap design to update our current design. Attached is our existing vehicle wrap design, which we would like to improve.
We want to modernise our design and have attached a few examples of designs we like.
We want to keep our color scheme to suit the existing design (red, blue, yellow). But we want a really bold stand out design.
Happy for a human mascot (electrician in blue uniform) - no animals.
Want to some how incorporate our light globe if possible.
Company Name: Copperline Wiring
Our slogan is: Need a really good electrician?
Services are Electrical, Air Conditioning, Solar Power
Phone number is: 1300 482 617
website is: www.copperlinewiring.com.au

We want it to be very bold and eye catching.

Target Market(s)

Home Owners

Industry/Entity Type

Electrical

Font styles to use
Serif
Sans Serif

Colors
0054AA
0677BA
7BADD7
CADEEF
E8F1F8
FFF300
FFF600
FEFA6F
FFFEC7
FFFEE8
EB3D1F
EC4F4E
F09395
F8D3D4
FCEDEE

Requirements
Must have
• Bold Design with our compay colors and details.
Nice to have
• Improve our existing design and try to incorporate our light bulb and a human mascot.
Should not have
• Animal mascot

```html
<!DOCTYPE html>
<html lang="en">
<head>
<meta charset="utf-8">
<title>Copperline Wiring – Van Wrap</title>
<link href="https://fonts.googleapis.com/css2?family=Anton&family=Fjalla+One&display=swap" rel="stylesheet">
<style>
  :root {
    --red: #EB3D1F;
    --red-deep: #b3121a;
    --red-dark: #8a0d12;
    --blue: #0054AA;
    --blue-mid: #0677BA;
    --blue-light: #7BADD7;
    --yellow: #FFF300;
    --yellow-soft: #FEFA6F;
    --orange: #f28a12;
    --white: #ffffff;
    --ink: #1d1d1f;
    --stage: #e7e8ea;
  }
  * { margin: 0; padding: 0; box-sizing: border-box; }
  html, body { width: 1200px; height: 675px; overflow: hidden; background: var(--stage); }
  .canvas { position: relative; width: 1200px; height: 675px; font-family: "Fjalla One", sans-serif; }

  .panel { position: absolute; top: 118px; height: 440px; border-radius: 18px; overflow: hidden; }
  .panel-side { left: 30px; width: 730px; }
  .panel-rear { left: 790px; width: 380px; }
  .panel svg.panel-bg { position: absolute; inset: 0; width: 100%; height: 100%; }

  .brand-name {
    position: absolute; font-family: "Anton", sans-serif; color: var(--white);
    text-transform: uppercase; letter-spacing: 0.5px; line-height: 1; white-space: nowrap;
    text-shadow: 3px 3px 0 var(--red-dark), -1px -1px 0 var(--red-dark);
  }
  .panel-side .brand-name { left: 200px; top: 48px; font-size: 56px; transform: rotate(-4deg); transform-origin: left top; }
  .panel-rear .brand-name { left: 22px; top: 26px; font-size: 40px; }

  .slogan { position: absolute; text-transform: uppercase; white-space: nowrap; }
  .panel-side .slogan { left: 14px; top: 318px; font-size: 18px; color: var(--white); transform: rotate(-15deg); transform-origin: left top; }
  .panel-rear .slogan { left: 24px; top: 82px; font-size: 16px; color: var(--yellow); }

  .services { position: absolute; list-style: none; text-transform: uppercase; color: var(--white); }
  .services li { display: flex; align-items: center; gap: 7px; text-shadow: 2px 2px 0 var(--red-dark); white-space: nowrap; }
  .services .dot { width: 12px; height: 12px; border-radius: 50%; background: var(--yellow); flex: none; box-shadow: 1px 1px 0 var(--red-dark); }
  .panel-side .services { left: 400px; top: 150px; font-family: "Anton", sans-serif; font-size: 32px; line-height: 1.65; }
  .panel-rear .services { left: 24px; top: 112px; font-size: 19px; line-height: 2.05; }

  .mascot { position: absolute; border-radius: 60px 60px 14px 14px;
    background: linear-gradient(180deg, #2d6fc4 0%, var(--blue) 55%, #1b3f8a 100%); }
  .panel-side .mascot { left: 272px; top: 140px; width: 112px; height: 200px; }
  .panel-rear .mascot { left: 222px; top: 120px; width: 136px; height: 256px; }

  .heritage { position: absolute; left: 190px; top: 356px; font-size: 16px; color: var(--white); text-transform: uppercase; white-space: nowrap; transform: rotate(3deg); }

  .contact { position: absolute; display: flex; gap: 16px; align-items: center; text-transform: uppercase; white-space: nowrap; }
  .contact span { display: flex; align-items: center; gap: 5px; }
  .contact svg { width: 15px; height: 15px; flex: none; }
  .panel-side .contact { left: 170px; top: 405px; font-size: 17px; color: var(--yellow); }
  .panel-rear .contact { left: 22px; top: 400px; font-size: 14px; color: var(--white); gap: 10px; }
  .panel-rear .contact svg { width: 13px; height: 13px; }
</style>
</head>
<body>
<main class="canvas">

  <section class="panel panel-side" aria-label="Van side panel">
    <svg class="panel-bg" viewBox="0 0 730 440" preserveAspectRatio="none" aria-hidden="true">
      <defs>
        <linearGradient id="sideRed" x1="0" y1="0" x2="1" y2="1">
          <stop offset="0" stop-color="#c61a18"/>
          <stop offset="0.6" stop-color="#EB3D1F"/>
          <stop offset="1" stop-color="#d4251a"/>
        </linearGradient>
        <linearGradient id="sideBlue" x1="0" y1="0" x2="0" y2="1">
          <stop offset="0" stop-color="#0677BA"/>
          <stop offset="1" stop-color="#0054AA"/>
        </linearGradient>
      </defs>
      <rect width="730" height="440" fill="url(#sideRed)"/>
      <path d="M0 300 C 200 320, 450 260, 730 40 L 730 110 C 480 300, 230 360, 0 345 Z" fill="#f28a12"/>
      <path d="M0 315 C 220 335, 470 290, 730 110 L 730 170 C 480 330, 240 380, 0 365 Z" fill="#FFF300"/>
      <path d="M0 370 C 250 385, 500 320, 730 190 L 730 440 L 0 440 Z" fill="url(#sideBlue)"/>
      <path d="M0 372 C 250 387, 500 322, 730 192" fill="none" stroke="#7BADD7" stroke-width="5"/>
      <rect x="0" y="395" width="730" height="45" fill="#2a1a14" opacity="0.85"/>
    </svg>

    <h1 class="brand-name">Copperline Wiring</h1>
    <div class="mascot" role="img" aria-label="Mascot illustration: smiling electrician in blue cap and uniform, giving a thumbs up with a tool over his shoulder"></div>
    <ul class="services">
      <li><i class="dot"></i>Electrical</li>
      <li><i class="dot"></i>Air Conditioning</li>
      <li><i class="dot"></i>Solar Power</li>
    </ul>
    <p class="slogan">Need a really good electrician?</p>
    <p class="heritage">Family owned &amp; operated since 1986</p>
    <p class="contact">
      <span><svg viewBox="0 0 16 16" aria-hidden="true"><path d="M4 1l3 3-2 2c1 2 3 4 5 5l2-2 3 3-2 3C7 15 1 9 1 3z" fill="currentColor"/></svg>1300 482 617</span>
      <span><svg viewBox="0 0 16 16" aria-hidden="true"><g fill="none" stroke="currentColor" stroke-width="1.5"><circle cx="8" cy="8" r="6.5"/><ellipse cx="8" cy="8" rx="3" ry="6.5"/><path d="M1.5 8h13"/></g></svg>www.copperlinewiring.com.au</span>
    </p>
  </section>

  <section class="panel panel-rear" aria-label="Van rear panel">
    <svg class="panel-bg" viewBox="0 0 380 440" preserveAspectRatio="none" aria-hidden="true">
      <rect width="380" height="440" fill="#EB3D1F"/>
      <path d="M0 300 C 120 260, 260 230, 380 250 L 380 440 L 0 440 Z" fill="#0054AA"/>
      <path d="M0 300 C 120 260, 260 230, 380 250" fill="none" stroke="#0677BA" stroke-width="8"/>
      <rect x="0" y="385" width="380" height="55" fill="#0054AA"/>
    </svg>

    <h2 class="brand-name">Copperline Wiring</h2>
    <p class="slogan">Need a really good electrician?</p>
    <ul class="services">
      <li><i class="dot"></i>Electrical</li>
      <li><i class="dot"></i>Air Conditioning</li>
      <li><i class="dot"></i>Solar Power</li>
    </ul>
    <div class="mascot" role="img" aria-label="Mascot illustration: smiling electrician in blue cap and uniform, giving a thumbs up with a tool over his shoulder"></div>
    <p class="contact">
      <span><svg viewBox="0 0 16 16" aria-hidden="true"><path d="M4 1l3 3-2 2c1 2 3 4 5 5l2-2 3 3-2 3C7 15 1 9 1 3z" fill="currentColor"/></svg>1300 482 617</span>
      <span><svg viewBox="0 0 16 16" aria-hidden="true"><g fill="none" stroke="currentColor" stroke-width="1.5"><circle cx="8" cy="8" r="6.5"/><ellipse cx="8" cy="8" rx="3" ry="6.5"/><path d="M1.5 8h13"/></g></svg>www.copperlinewiring.com.au</span>
    </p>
  </section>

</main>
</body>
</html>
```